BUSINESS CARD DESIGN

NAME- TODD MASVERIK
PHONE NUMER - 808- 451-7082
EMAIL- OFFICE@VORLINDE-GRADEWAY.COM
BACK OF CARD- SPEACIALIZES IN LAND CLEARING, FORESTRY MUCLHING AND EXCAVATION

Contact Information for Business Card

NAME- TODD MASVERIK PHONE NUMER - 808- 451-7082 EMAIL- OFFICE@VORLINDE-GRADEWAY.COM BACK OF CARD- SPEACIALIZES IN LAND CLEARING , MUCLHING AND EXCAVATION

```html
<!DOCTYPE html>
<html lang="en">
<head>
<meta charset="UTF-8">
<title>Vorlinde Gradeway – Business Card</title>
<link href="https://fonts.googleapis.com/css2?family=Poppins:wght@300;400;600;800&display=swap" rel="stylesheet">
<style>
  :root {
    --gold: #f2a900;
    --ink: #070707;
    --paper: #ffffff;
    --paper-shade: #ececec;
    --grey-text: #4a4a4a;
    --backdrop: #e9e6e1;
  }
  * { margin: 0; padding: 0; box-sizing: border-box; }
  html, body {
    width: 1200px; height: 900px; overflow: hidden;
    background: var(--backdrop);
    font-family: "Poppins", sans-serif;
  }
  .canvas {
    width: 1200px; height: 900px;
    display: flex; flex-direction: column;
    align-items: center; justify-content: center; gap: 44px;
  }
  .card {
    width: 640px; height: 366px; position: relative; overflow: hidden;
    box-shadow: 0 10px 28px rgba(0,0,0,.22);
  }

  /* Back of card */
  .card--back { background: var(--ink); display: flex; align-items: center; justify-content: center; }
  .brand-mark {
    display: flex; align-items: center; gap: 14px;
    color: var(--gold); font-weight: 600; font-size: 26px; letter-spacing: 2px;
  }
  .brand-mark__dot { width: 22px; height: 22px; border-radius: 50%; background: currentColor; }

  /* Front of card */
  .card--front { background: linear-gradient(115deg, var(--paper) 0%, var(--paper) 45%, var(--paper-shade) 70%, var(--paper) 100%); }
  .lockup {
    position: absolute; left: 40px; top: 96px; width: 250px;
    text-align: center; color: var(--ink);
  }
  .lockup .brand-mark { color: var(--ink); font-size: 22px; justify-content: center; letter-spacing: 1.5px; }
  .lockup .brand-mark__dot { width: 18px; height: 18px; }
  .lockup__rule { height: 1.5px; background: var(--ink); margin: 8px 0; }
  .lockup__sub { font-weight: 600; font-size: 11px; letter-spacing: 7px; }
  .lockup__phone { font-weight: 600; font-size: 11px; letter-spacing: 9px; margin-top: 2px; }

  .contact {
    position: absolute; right: 34px; top: 92px; text-align: right;
  }
  .contact__name {
    color: var(--gold); font-weight: 800; font-size: 25px; letter-spacing: 1px;
    margin-bottom: 10px;
  }
  .contact__line {
    display: flex; align-items: center; justify-content: flex-end; gap: 8px;
    color: var(--grey-text); font-weight: 300; font-size: 17px; line-height: 1.7;
  }
  .contact__line svg { width: 15px; height: 15px; fill: var(--ink); }

  .specialty-band {
    position: absolute; left: 0; right: 0; bottom: 0; height: 74px;
    background: var(--ink); border-top: 4px solid var(--gold);
    display: flex; align-items: center; justify-content: center;
    color: var(--gold); font-size: 17px; font-weight: 400;
  }
</style>
</head>
<body>
<main class="canvas">
  <section class="card card--back" aria-label="Card back">
    <div class="brand-mark"><span class="brand-mark__dot"></span>VORLINDE GRADEWAY</div>
  </section>

  <section class="card card--front" aria-label="Card front">
    <div class="lockup">
      <div class="brand-mark"><span class="brand-mark__dot"></span>VORLINDE GRADEWAY</div>
      <div class="lockup__rule"></div>
      <div class="lockup__sub">LLC · HAWAII</div>
      <div class="lockup__rule"></div>
      <div class="lockup__phone">808-451-7082</div>
    </div>

    <div class="contact">
      <div class="contact__name">TODD MASVERIK</div>
      <div class="contact__line">808- 451-7082
        <svg viewBox="0 0 24 24" aria-hidden="true"><path d="M6.6 10.8a15 15 0 0 0 6.6 6.6l2.2-2.2c.3-.3.7-.4 1-.2 1.1.4 2.3.6 3.6.6.6 0 1 .4 1 1V20c0 .6-.4 1-1 1A17 17 0 0 1 3 4c0-.6.4-1 1-1h3.5c.6 0 1 .4 1 1 0 1.3.2 2.5.6 3.6.1.3 0 .7-.2 1z"/></svg>
      </div>
      <div class="contact__line">office@vorlinde-gradeway.com
        <svg viewBox="0 0 24 24" aria-hidden="true"><path d="M2 5h20v14H2zm2 2v.4l8 5.2 8-5.2V7z"/></svg>
      </div>
    </div>

    <div class="specialty-band">Speacializes In - &nbsp;Land Clearing, Muclhing And Excavation</div>
  </section>
</main>
</body>
</html>
```